Become a real French Pastry chef with an easy 3 step pastry kit box.

The company is specialized in French pastries and the boxes will be sold online, and retail stores. The goal is for anyone who likes to be creative and crafty to create and bake their own traditional french pastry in 3 easy steps right at home. French pastries can be known to take hours to bake. These boxes allow you to make them very quickly, no hassle and they results taste amazing. All the ingredients are from FRANCE. Everything you need is in the box, All you need is water! The box design desired is elegant, simple, glamorous but yet eye catchy for retail distribution. This is a kit box with pre scaled ingredients to make your own eclairs. Box dimensions are 8x6x2.
Updates

Target Market(s)

Middle Aged, middle to upper class housewives who enjoy cooking and baking

Industry/Entity Type

Bakery

Font styles to use
Decorative
Script

Colors

Designer to choose colors to be used in the design.

Requirements
Must have
• This box will be called "The eclair kit by {logo}, or {logo} presents the Eclair kit.
• Has to have the instructions (attached document)
• "This box contains: 4 éclair shells, powder pouch, icing bag, pipping bag and pipping tip"
• Net weight 245g
• Nutrition label (attached)
Nice to have
• An eclair on it.

```html
<!DOCTYPE html>
<html lang="en">
<head>
<meta charset="utf-8">
<title>The Eclair Kit – Box Dieline</title>
<link href="https://fonts.googleapis.com/css2?family=Open+Sans:wght@400;600;700&family=Berkshire+Swash&family=Playfair+Display:ital,wght@1,500&family=Arimo:wght@400;700&display=swap" rel="stylesheet">
<style>
  :root{
    --cocoa:#412e2c;
    --sand:#e6d19b;
    --cream:#f2efe6;
    --ink:#5a2a1e;
    --title:#6b2a14;
    --accent-red:#b3261e;
    --sky:#8fc7e8;
    --brand:#3a64c8;
    --cut:#7fd16a;
    --paper:#ffffff;
  }
  html,body{margin:0;padding:0;overflow:hidden;background:var(--paper);}
  .canvas{position:relative;width:1200px;height:1200px;overflow:hidden;background:var(--paper);font-family:"Open Sans",sans-serif;color:var(--ink);}
  .dieline{position:absolute;left:0;top:0;}
  .front-photo{position:absolute;left:382px;top:186px;width:450px;height:342px;
    background:linear-gradient(180deg,#f6f4f2 0%,#ebe7e4 45%,#e9e2da 70%,#c9a470 82%,#4a2a1f 92%,#3d241b 100%);}
  .brand{position:absolute;left:402px;top:278px;width:196px;display:flex;align-items:center;gap:8px;
    font-family:"Open Sans",sans-serif;font-weight:600;font-size:20px;line-height:1.1;color:var(--brand);}
  .brand-dot{width:16px;height:16px;border-radius:50%;background:var(--sky);flex:none;}
  .presents{position:absolute;left:616px;top:244px;font-family:"Playfair Display",serif;font-style:italic;font-weight:500;font-size:20px;color:var(--accent-red);}
  .kit-title{position:absolute;left:608px;top:276px;width:212px;font-family:"Berkshire Swash",cursive;font-size:32px;line-height:40px;color:var(--title);white-space:nowrap;}
  .title-rule{position:absolute;left:616px;top:329px;width:186px;height:2px;background:linear-gradient(90deg,transparent,var(--sky) 20%,var(--sky) 80%,transparent);}

  .nutrition{position:absolute;left:376px;top:548px;width:460px;height:74px;border:1px solid #7a6a55;box-sizing:border-box;
    font-family:"Arimo",sans-serif;font-size:4.6px;line-height:1.35;color:#222;display:grid;grid-template-columns:82px 128px 128px 1fr;gap:4px;padding:2px 3px;}
  .nutrition h3{margin:0;font-size:12px;line-height:.95;font-weight:700;}
  .nutrition .col{border-top:2px solid #222;}
  .nutrition .col div{display:flex;justify-content:space-between;border-bottom:.5px solid #444;}
  .nutrition b{font-weight:700;}
  .nutrition .note{font-size:3.6px;}
  .contents{position:absolute;left:380px;top:628px;font-size:9px;line-height:14px;color:#3a2a22;}

  .instructions{position:absolute;left:370px;top:678px;width:474px;box-sizing:border-box;padding:0 12px;text-align:center;color:var(--ink);}
  .step h2{margin:0 0 4px;font-size:13px;font-weight:700;}
  .step p{margin:0 0 12px;font-size:12.2px;line-height:17px;}
  .ingredients{position:absolute;left:383px;top:910px;width:340px;font-size:7.6px;line-height:11.2px;color:var(--ink);white-space:nowrap;}
  .ingredients p{margin:0;}
</style>
</head>
<body>
<div class="canvas">
  <svg class="dieline" width="1200" height="1200" viewBox="0 0 1200 1200" aria-hidden="true">
    <path d="M226,528 L226,235 Q226,200 250,195 L258,193 Q270,45 360,34 L852,34 Q942,45 954,193 L962,195 Q986,200 986,235 L986,528" fill="none" stroke="var(--cut)" stroke-width="1"/>
    <path d="M198,660 L198,676 M1014,660 L1014,676 M198,1008 L198,1024 M1014,1008 L1014,1024 M360,1152 L360,1166 L852,1166 L852,1152" fill="none" stroke="var(--cut)" stroke-width="1"/>
    <path d="M370,186 L370,44 Q272,52 242,172 L246,186 Z" fill="var(--sand)"/>
    <path d="M842,186 L842,44 Q940,52 970,172 L966,186 Z" fill="var(--sand)"/>
    <rect x="370" y="44" width="472" height="142" fill="var(--cocoa)"/>
    <path d="M382,188 L262,212 Q238,218 238,242 L238,492 Q238,510 260,510 L382,512 Z" fill="var(--cocoa)"/>
    <path d="M830,188 L950,212 Q974,218 974,242 L974,492 Q974,510 952,510 L830,512 Z" fill="var(--cocoa)"/>
    <rect x="204" y="528" width="804" height="144" rx="6" fill="var(--sand)"/>
    <rect x="204" y="1010" width="804" height="142" rx="6" fill="var(--sand)"/>
    <rect x="374" y="1012" width="464" height="140" fill="var(--cocoa)"/>
    <path d="M78,672 L370,672 L370,1010 L78,1010 Q72,1010 72,1002 L72,880 Q64,878 64,870 L64,780 Q64,744 72,742 L72,680 Q72,672 78,672 Z" fill="var(--cocoa)"/>
    <path d="M1136,672 L844,672 L844,1010 L1136,1010 Q1142,1010 1142,1002 L1142,880 Q1150,878 1150,870 L1150,780 Q1150,744 1142,742 L1142,680 Q1142,672 1136,672 Z" fill="var(--cocoa)"/>
    <rect x="370" y="672" width="474" height="338" fill="var(--cream)"/>
  </svg>

  <div class="front-photo" role="img" aria-label="Photo of a chocolate-glazed éclair on a soft white background"></div>
  <div class="brand"><span class="brand-dot"></span><span>Maison Douce Bakery</span></div>
  <div class="presents">Presents</div>
  <div class="kit-title">The Eclair Kit</div>
  <div class="title-rule"></div>

  <section class="nutrition">
    <div><h3>Nutrition<br>Facts</h3>Serving Size 1 éclair (106g)<br>Servings Per Container 4<br><b>Calories</b> 292</div>
    <div class="col">
      <div><b>Total Fat</b> 16g<b>25%</b></div>
      <div>&nbsp;Saturated Fat 4.1g<b>21%</b></div>
      <div>&nbsp;Trans Fat 0g<span></span></div>
      <div>&nbsp;Polyunsaturated Fat 3.9g<span></span></div>
      <div>&nbsp;Monounsaturated Fat 6g<span></span></div>
      <div><b>Cholesterol</b> 127mg<b>42%</b></div>
      <div>Vitamin A 10% • Calcium 6%<span></span></div>
    </div>
    <div class="col">
      <div><b>Potassium</b> 3mg<b>0%</b></div>
      <div><b>Sodium</b> 337mg<b>14%</b></div>
      <div><b>Total Carbohydrate</b> 24g<b>8%</b></div>
      <div>&nbsp;Dietary Fiber 0.6g<b>2%</b></div>
      <div>&nbsp;Sugars 7g<span></span></div>
      <div><b>Protein</b> 6g<b>12%</b></div>
      <div>Iron 6% • Vitamin D 9%<span></span></div>
    </div>
    <div class="note">* Percent Daily Values are based on a 2,000 calorie diet. Your values may be higher or lower depending on your calorie needs. Total fat less than 65g, sodium less than 2400mg.</div>
  </section>
  <div class="contents">This Box Contains :<br>4 éclair shells • powder pouch • icing bag • pipping bag • pipping tip<br>Net weight 245g</div>

  <section class="instructions">
    <div class="step"><h2>Step 1</h2><p>Mix powder patch with 1 cup of cold water, mix for 2 minutes on high speed.<br>Let the custard rest in fridge for 15 minutes</p></div>
    <div class="step"><h2>Step 2</h2><p>Place pipping tip in pipping bag. Poor custard in bag before cutting the tip off<br>of it off. Pipe custard inside eclair by slightly pressing on flat side of the shell<br>in 3 separate areas for a more uniform filling. Do not over fill or shell will crack.</p></div>
    <div class="step"><h2>Step 3</h2><p>Place icing in warm water for 2 minutes, cut bag at an angle, then poor on<br>top of eclair</p></div>
  </section>
  <section class="ingredients">
    <p>Ingredients :</p>
    <p>Eclair shell: wheat flour(gluten), butter fat 26%, egg, water, potassium and sodium<br>diphosphates, sodium carbonates, salt, sorbitol.</p>
    <p>Powder: sugar, modified potato starch(E 1414), whole milk powder, lactose and<br>milk proteins, thickeners : calcium lactate, disodium phosphate, disodium<br>diphosphate, sodium alginate, carrageenan, artificial and natural flavors:<br>vanillin, caramel, colors: E 102, E 110 (may contain cocoa powder)</p>
    <p>Icing: sugar, glucose syrup, water (may contain cocoa powder)</p>
  </section>
</div>
</body>
</html>
```